Web-site design for company trading in chemicals & lubricants

We need a standard 5 page web-site designed for our company based in Dubai, UAE.
The web-site should highlight our capacity to store material as well as distribute the same. The products we sell are basic chemicals - packed in bags as well as drums. Bags are big bags - 25 kgs each as well as drums - 200 litres each. We want to highlight the fact that we huge stocks of this material & can deliver by sea & road,
Please use this site as a ref - http://www.torvane-chemicals.co.uk/
Besides this, we need a page dedicated to finished products that we are selling for use in the auto industry - lubricants, motor oils,brake-fluids, greases, coolants etc. This are packed in large drums as well as small cans.
It would be nice if the site could immediately also provide a ref. to our location - Dubai or that we are based in the Middle East.
We will provide our company logo for reference

```html
<!DOCTYPE html>
<html lang="en">
<head>
<meta charset="utf-8">
<title>Dunevar – Chemicals &amp; Lubricants</title>
<link rel="stylesheet" href="https://fonts.googleapis.com/css2?family=PT+Sans:wght@400;700&family=Saira:wght@500;600&display=swap">
<style>
  :root {
    --brown: #5a2d14;
    --olive: #7a6410;
    --gold: #b3912a;
    --bullet: #b8922d;
    --panel: #dfdfdf;
    --topbar: #e4e4e2;
    --text: #444444;
    --nav-text: #5a2d14;
    --white: #ffffff;
  }
  * { margin: 0; padding: 0; box-sizing: border-box; }
  html, body { width: 1200px; height: 1200px; overflow: hidden; background: var(--white); }
  body { font-family: "PT Sans", Tahoma, sans-serif; color: var(--text); }
  .site { position: relative; width: 1000px; height: 1000px; transform: scale(1.2); transform-origin: 0 0; overflow: hidden;
    background: linear-gradient(#fff 0 60%, #f6f6f6 100%); }

  .topbar { position: absolute; left: 0; top: 0; width: 1000px; height: 38px; background: var(--topbar); }
  .social { position: absolute; right: 24px; top: 8px; display: flex; gap: 10px; }
  .social span { width: 21px; height: 21px; border-radius: 50%; background: #9a9a9a; display: block; }

  .header { position: absolute; left: 0; top: 38px; width: 1000px; height: 127px;
    background: linear-gradient(#ffffff, #ececec); border-bottom: 5px solid var(--brown); height: 132px; }
  .brand { position: absolute; left: 25px; top: 62px; display: flex; align-items: center; gap: 14px; }
  .brand-name { font-family: "Saira", sans-serif; font-weight: 600; font-size: 50px; letter-spacing: 3px; color: var(--brown); line-height: 1; }
  .brand-mark { width: 26px; height: 26px; border-radius: 50%; background: var(--olive); }

  .nav { position: absolute; left: 399px; top: 78px; display: flex; list-style: none; }
  .nav li { height: 50px; line-height: 54px; font-size: 14px; text-transform: uppercase; color: var(--nav-text); text-align: center; width: 108px; }
  .nav li.active { width: 121px; background: var(--brown); color: var(--white); border-radius: 6px 6px 0 0; margin-right: 10px; }

  .side-box { position: absolute; left: 6px; width: 184px; background: var(--panel); }
  .box-title { height: 39px; line-height: 44px; text-align: center; color: var(--white); font-size: 15px; text-transform: uppercase; }
  .title-brown { background: var(--brown); }
  .title-olive { background: var(--olive); }
  .title-gold { background: var(--gold); }
  .link-list { list-style: none; padding-top: 8px; }
  .link-list li { height: 30px; line-height: 24px; font-size: 11px; padding-left: 39px; position: relative; color: var(--text); }
  .link-list li::before { content: ""; position: absolute; left: 25px; top: 10px; width: 4px; height: 4px; background: var(--bullet); }

  .gallery { position: absolute; left: 198px; top: 179px; display: flex; gap: 3px; }
  .gallery div { width: 197px; height: 329px; }
  .photo-drums { background: linear-gradient(160deg, #5a5e9a, #2e2f7a 60%, #1c1d50); }
  .photo-racks { background: linear-gradient(180deg, #c9c7c0, #8e8a82 50%, #b34a3c 100%); }
  .photo-tubes { background: linear-gradient(100deg, #c86a7a, #e6dede 40%, #7fb4d2 60%, #d8cf6a); }
  .photo-tablets { background: linear-gradient(150deg, #e2c45a, #f2efe4 45%, #d6d6d6); }

  .divider { position: absolute; left: 0; top: 513px; width: 1000px; height: 2px; background: #e6e6e6; }

  .main { position: absolute; left: 210px; top: 526px; width: 568px; }
  .main h1 { font-family: "Saira", sans-serif; font-weight: 500; font-size: 28px; color: #7a5a14; letter-spacing: 0.5px; line-height: 32px; margin-bottom: 18px; }
  .main p { font-size: 12.2px; line-height: 20px; margin-bottom: 20px; }

  .news { position: absolute; left: 798px; top: 521px; width: 197px; height: 329px; background: var(--panel); }
  .news p { padding: 18px 14px 0 20px; font-size: 12.2px; line-height: 20px; }
  .read-more { display: block; padding: 10px 0 0 20px; font-size: 13px; font-weight: 700; color: #555; }
</style>
</head>
<body>
<div class="site">
  <div class="topbar">
    <div class="social"><span></span><span></span><span></span><span></span></div>
  </div>

  <header class="header">
    <div class="brand"><span class="brand-name">DUNEVAR</span><span class="brand-mark"></span></div>
    <ul class="nav">
      <li class="active">Home</li>
      <li>Page 2</li>
      <li>Page 3</li>
      <li>Page 4</li>
      <li>Page 5</li>
    </ul>
  </header>

  <aside class="side-box" style="top:179px; height:329px;">
    <div class="box-title title-brown">Lorum Ipsum</div>
    <ul class="link-list">
      <li>Lorem ipsum dolor sit</li><li>Lorem ipsum dolor sit</li><li>Lorem ipsum dolor sit</li>
      <li>Lorem ipsum dolor sit</li><li>Lorem ipsum dolor sit</li><li>Lorem ipsum dolor sit</li>
      <li>Lorem ipsum dolor sit</li><li>Lorem ipsum dolor sit</li><li>Lorem ipsum dolor sit</li>
    </ul>
  </aside>

  <div class="gallery">
    <div class="photo-drums" role="img" aria-label="Worker filling blue 200 litre chemical drums in a warehouse"></div>
    <div class="photo-racks" role="img" aria-label="Long aisle of red warehouse storage racks"></div>
    <div class="photo-tubes" role="img" aria-label="Glass test tubes holding coloured liquids"></div>
    <div class="photo-tablets" role="img" aria-label="Close view of white tablets"></div>
  </div>

  <div class="divider"></div>

  <aside class="side-box" style="top:521px; height:329px;">
    <div class="box-title title-olive">Lorum Ipsum</div>
    <ul class="link-list">
      <li>Lorem ipsum dolor sit</li><li>Lorem ipsum dolor sit</li><li>Lorem ipsum dolor sit</li>
      <li>Lorem ipsum dolor sit</li><li>Lorem ipsum dolor sit</li><li>Lorem ipsum dolor sit</li>
      <li>Lorem ipsum dolor sit</li><li>Lorem ipsum dolor sit</li><li>Lorem ipsum dolor sit</li>
    </ul>
  </aside>

  <aside class="side-box" style="top:862px; height:160px;">
    <div class="box-title title-gold">Lorum Ipsum</div>
    <ul class="link-list">
      <li>Lorem ipsum dolor sit</li><li>Lorem ipsum dolor sit</li><li>Lorem ipsum dolor sit</li>
      <li>Lorem ipsum dolor sit</li>
    </ul>
  </aside>

  <main class="main">
    <h1>WELCOME TO DUNEVAR</h1>
    <p>Lorem ipsum dolor sit amet, consectetur adipiscing elit. Ut nec enim massa. Donec molestie, arcu sed tristique aliquam, nunc justo molestie massa, ut luctus libero ipsum et sapien. Etiam vehicula, leo sit amet dictum lobortis, nibh velit placerat eros, facilisis sodales sapien arcu vitae nisi. Nulla in dui dolor. Ut felis orci, sagittis tincidunt bibendum fermentum, consectetur nec quam. Sed consequat faucibus auctor. Nulla dapibus urna sed nibh ullamcorper vel mattis lacus viverra. Praesent fringilla ornare ipsum, non elementum nunc elementum ut. Vestibulum nec velit metus, pretium vehicula enim. Praesent sed nibh orci, ac suscipit quam. Fusce elit ipsum, malesuada a venenatis vitae, condimentum sit amet turpis. Morbi ac dui ac turpis placerat rhoncus. Vivamus dignissim rhoncus quam, eu porta nisl ultricies vel. Etiam a eros sed ante viverra dapibus. Etiam nibh turpis, dignissim quis ultricies sed, facilisis et orci. Suspendisse condimentum est sed massa cursus ut molestie urna hendrerit.</p>
    <p>Cras magna lorem, accumsan et gravida eu, vestibulum a risus. Duis pretium auctor massa et semper. Quisque quis nisi nisl. Nulla euismod, odio quis elementum ornare, magna eros molestie purus, a commodo augue nibh non ante. Sed sed urna vel dui mollis tempor sit amet at quam. Morbi a magna diam. Aliquam ultricies, velit sed cursus vestibulum, purus diam aliquam neque, et varius lacus felis eget mauris. Nulla facilisi. Suspendisse facilisis malesuada sem, id volutpat lectus lacinia id. Nullam eget orci nisl, eu laoreet dui. Sed dictum leo mattis leo semper a auctor dolor scelerisque.</p>
    <p>Cum sociis natoque penatibus et magnis dis parturient montes, nascetur ridiculus mus. Morbi justo orci, tempus nec consectetur sit amet, euismod eget erat. Nam commodo, mauris volutpat pharetra viverra, sapien metus tempor risus, eu rhoncus orci eros non ipsum. In varius, tortor at consectetur pharetra, neque lorem tincidunt nisi, vel tempor purus arcu eget nunc.</p>
  </main>

  <aside class="news">
    <div class="box-title title-olive">Latest News</div>
    <p>Lorem ipsum dolor sit amet, consectetur adipiscing elit. Ut nec enim massa. Donec molestie, arcu sed tristique aliquam, nunc justo molestie massa, ut luctus libero ipsum et sapien. Etiam vehicula, leo sit amet dictum lobortis, nibh velit placerat eros, facilisis sodales sapien arcu vitae nisi. Nulla in dui dolor.</p>
    <span class="read-more">Read More</span>
  </aside>
</div>
</body>
</html>
```